Upcoming Guitar Teacher needs a Rock Star PDF of online course

We are in the process of revising our online course and need to make more visually appealing PDFs for students. We help regular folks learn how to play their favorite songs on the guitar. This design is a sign-up bonus for fast responders to our CTA. We would like to see designs that incorporate our colors, if possible. The final design should be clean and simple.
Attached is a copy of my YouTube banner where you can get the colors from and my logo. I have also attached a clean looking example for you to refer to. Here is an additional resource provided as another example of how the final product should look: https://files.cloudvault-share.net/f/8KQZ2rLmTx4PaW7nBv3YcD1eHs6Ju0Gi/view
The visuals will all need to be unified.

The main document is in Google Docs below. https://pages.writespace-online.net/doc/d/7HtRk2PqLm9XzVa4NbYc3WsEd8FgJu1KoLi5MnBvCx6/edit?mode=share

Here is an updated Google Docs link that is not restricted. https://pages.writespace-online.net/doc/d/7HtRk2PqLm9XzVa4NbYc3WsEd8FgJu1KoLi5MnBvCx6/edit?mode=share

• SOCIAL MEDIA LINKS:

Instagram: https://www.pictofeed-social.net/maple.hollow.music/
Facebook: https://www.friendwall-social.net/maplehollowmusic
Twitter: https://chirpline-social.net/ben_castrow
YouTube: https://www.vidstream-hub.net/channel/VKP3nhtrxDaLMQ8ZcTEvbWkS

```html
<!DOCTYPE html>
<html lang="en">
<head>
<meta charset="utf-8">
<title>Your Title Here – Course Guide</title>
<link rel="stylesheet" href="https://fonts.googleapis.com/css2?family=Bebas+Neue&family=Lobster&family=Poppins:wght@400;500;600;700&display=swap">
<style>
  :root {
    --red: #c9362c;
    --red-deep: #b3332b;
    --ink: #1c1c1c;
    --text: #222222;
    --paper: #ffffff;
    --backdrop: #8a8a8a;
    --peach: #f6d2c2;
    --cloud: #d9d6d3;
    --orange: #e98a4a;
  }
  * { box-sizing: border-box; margin: 0; padding: 0; }
  html, body { width: 1200px; height: 582px; overflow: hidden; }
  body { background: var(--backdrop); font-family: "Poppins", sans-serif; position: relative; }

  .page { position: absolute; top: 34px; width: 344px; height: 486px; background: var(--paper); overflow: hidden; }
  .page--cover { left: 32px; background: linear-gradient(180deg, var(--cloud) 0%, #ebe6e2 45%, var(--peach) 75%, #fbe8df 100%); }
  .page--contents { left: 433px; }
  .page--lesson { left: 819px; }

  /* Cover */
  .cover-glow { position: absolute; left: 220px; top: 0; width: 124px; height: 60px;
    background: radial-gradient(ellipse at 70% 40%, var(--orange) 0%, rgba(233,138,74,0) 70%); }
  .cover-photo { position: absolute; left: 60px; top: 32px; width: 230px; height: 270px;
    background: radial-gradient(ellipse at 50% 45%, #5a4a40 0%, #8c7b70 35%, #d8d2cd 70%, rgba(230,226,222,0) 100%); border-radius: 40% 40% 30% 30%; }
  .cover-crowd { position: absolute; left: 0; bottom: 0; width: 344px; height: 170px;
    background: linear-gradient(180deg, rgba(232,150,130,0) 0%, rgba(232,150,130,.45) 55%, rgba(240,190,170,.3) 100%); }
  .cover-badge { position: absolute; left: 126px; top: 200px; width: 96px; height: 96px; border-radius: 50%;
    background: #f4ead8; border: 5px solid var(--red); display: flex; align-items: center; justify-content: center; text-align: center;
    font-weight: 700; font-size: 10px; line-height: 1.15; color: var(--red); padding: 10px; }
  .cover-title { position: absolute; left: 0; width: 344px; top: 296px; text-align: center;
    font-family: "Bebas Neue", sans-serif; font-weight: 400; font-size: 88px; line-height: 1; color: var(--ink); letter-spacing: -1px; }
  .cover-script { position: absolute; left: 0; width: 344px; top: 366px; text-align: center;
    font-family: "Lobster", cursive; font-size: 80px; line-height: 1; color: var(--red); }
  .cover-tagline { position: absolute; left: 0; width: 344px; top: 458px; text-align: center;
    font-size: 10.5px; font-weight: 500; color: var(--ink); letter-spacing: .3px; }

  /* Inner frame */
  .sheet { position: absolute; top: 16px; left: 18px; width: 306px; height: 429px; background: var(--paper);
    box-shadow: 0 0 4px rgba(0,0,0,.25); }
  .folio { position: absolute; left: 313px; top: 453px; width: 17px; height: 16px; background: var(--red);
    color: #fff; font-size: 10px; line-height: 16px; text-align: center; }
  .folio-rule-h { position: absolute; left: 286px; top: 470px; width: 52px; height: 1px; background: var(--red); }
  .folio-rule-v { position: absolute; left: 333px; top: 428px; width: 1px; height: 48px; background: var(--red); }

  /* Contents */
  .contents-title { position: absolute; left: 8px; top: 6px; font-family: "Bebas Neue", sans-serif; font-weight: 400;
    font-size: 62px; line-height: .8; color: var(--red); letter-spacing: -.5px; }
  .contents-panel { position: absolute; left: 9px; top: 54px; width: 170px; height: 366px; background: var(--red-deep); }
  .contents-list { list-style: none; position: absolute; left: 11px; top: 14px; }
  .contents-list li { color: #fff; font-size: 11px; height: 24.2px; }

  /* Lesson */
  .lesson-band { position: absolute; left: 0; top: 0; }
  .lesson-body { position: absolute; left: 12px; top: 0; width: 284px; color: var(--text); }
  .lesson-heading { position: absolute; top: 35px; left: 0; color: var(--red); font-weight: 700; font-size: 10.5px; white-space: nowrap; }
  .checklist { position: absolute; top: 55px; left: 0; list-style: none; font-size: 8px; line-height: 1.15; }
  .checklist li::before { content: "✓"; color: var(--red); font-size: 6px; margin-right: 2px; }
  .para { position: absolute; left: 0; width: 286px; font-size: 7.9px; line-height: 1.15; }
  .section-head { position: absolute; left: 0; display: flex; align-items: center; }
  .section-icon { width: 21px; height: 21px; border-radius: 50%; border: 1.5px solid var(--red); background: #fff;
    display: flex; align-items: center; justify-content: center; position: relative; z-index: 1; }
  .section-icon span { width: 14px; height: 14px; border-radius: 50%; background: var(--red); display: block; }
  .section-label { border: 1px dashed var(--red); border-left: none; color: var(--red); font-size: 8.6px; font-weight: 500;
    padding: 2px 3px 2px 4px; margin-left: -2px; white-space: nowrap; }
  .section-copy { position: absolute; left: 0; width: 284px; text-align: justify; font-size: 7.2px; line-height: 1.17; }
</style>
</head>
<body>

<section class="page page--cover">
  <div class="cover-glow"></div>
  <div class="cover-photo" role="img" aria-label="Photo of the guitar teacher playing an acoustic guitar among clouds"></div>
  <div class="cover-crowd" role="img" aria-label="Faded concert crowd with raised hands"></div>
  <div class="cover-badge">Maple Hollow Music</div>
  <h1 class="cover-title">YOUR TITLE</h1>
  <div class="cover-script">Here</div>
  <p class="cover-tagline">TO MASTER STRUMMING LIKE A ROCK STAR!</p>
</section>

<section class="page page--contents">
  <div class="sheet">
    <h2 class="contents-title">CONTENT</h2>
    <div class="contents-panel">
      <ul class="contents-list">
        <li>- Welcome...</li>
        <li>- Lorem ipsum</li>
        <li>- Lorem ipsum</li>
        <li>- Lorem ipsum</li>
        <li>- Lorem ipsum</li>
        <li>- Lorem ipsum</li>
        <li>- Lorem ipsum</li>
        <li>- Lorem ipsum</li>
        <li>- Lorem ipsum</li>
        <li>- Lorem ipsum</li>
        <li>- Lorem ipsum</li>
        <li>- Lorem ipsum</li>
        <li>- Lorem ipsum</li>
      </ul>
    </div>
  </div>
  <div class="folio">2</div>
  <div class="folio-rule-h"></div>
  <div class="folio-rule-v"></div>
</section>

<section class="page page--lesson">
  <svg class="lesson-band" width="344" height="486" viewBox="0 0 344 486" aria-hidden="true">
    <polygon points="0,241 344,138 344,362 0,467" fill="var(--red)"/>
  </svg>
  <div class="sheet">
    <div class="lesson-body">
      <h2 class="lesson-heading">What you will need one of the following:</h2>
      <ul class="checklist">
        <li>A pick</li>
        <li>Your thumb</li>
        <li>The back of your fingernails</li>
      </ul>
      <p class="para" style="top:92px">Can you count to four? Can you do it again? Then you can play rhythm!</p>
      <p class="para" style="top:110px">Okay, it's not that easy. But it is that simple.</p>
      <p class="para" style="top:128px">Before we get started, I want to cover a few necessary things that will help along the way. These are several mistakes that folks do when just starting to learn how to strum effectively.</p>

      <div class="section-head" style="top:168px">
        <div class="section-icon"><span></span></div>
        <div class="section-label">TAKE YOUR PICK</div>
      </div>
      <p class="section-copy" style="top:195px">While you can play with your thumb and fingers, a pick will definitely give you an advantage. To hold a pick, use your thumb and index finger only. The pick should be facing the same way as your index finger, not your thumb. Hold pick closely to tip. Not like a dead mouse. This will help prevent dropping your pick into the soundhole (which stinks and should be avoided. It's a rear pain in the neck retrieving them inside an acoustic guitar).</p>

      <div class="section-head" style="top:256px">
        <div class="section-icon"><span></span></div>
        <div class="section-label">FINGER IT OUT - USING FINGERS INSTEAD OF PICKS</div>
      </div>
      <p class="section-copy" style="top:283px">Make like you are holding a pick. Use your index fingernail when you strum down, your thumbnail when you strum up, from the elbow</p>

      <div class="section-head" style="top:311px">
        <div class="section-icon"><span></span></div>
        <div class="section-label">WITH OR WITHOUT YOU</div>
      </div>
      <p class="section-copy" style="top:338px">People usually prefer one or the other, and will sometimes forsake the other. I had a student who would only use his thumb for any kind of strumming. Then he wanted to learn a very fast song (Stormbreaker by The Voltage) and he just couldn't do it. He had six months of playing under his belt and had to start learning how to use a pick for the first time. It was awkward for him.<br>My suggestion is to do both. In the beginning, you should learn and do both regularly. It's like learning two languages at the same time.</p>
    </div>
  </div>
  <div class="folio">2</div>
  <div class="folio-rule-h"></div>
  <div class="folio-rule-v"></div>
</section>

</body>
</html>
```